I am looking for a book cover designs. The title of the book is "Ways to stand out and where your habits slip"

the book is not too formal but it is also not informal.

I wish for the title to be easily readable and capturing, especially the "ways to stand out" part.

the book should also include the author name: Tobar Kessly

everyone

• Full title and author name: Tobar Kessly
• There is a chapter that is called "turn the lamp inward", if you wish to do an illustration as part of the cover then perhaps that can give you an idea of what to go with.
• anything that takes attention away from the title.Also should not include any photographs.

```html
<!DOCTYPE html>
<html lang="en">
<head>
<meta charset="utf-8">
<title>Ways to Stand Out and Where Your Habits Slip — Book Cover</title>
<link rel="stylesheet" href="https://fonts.googleapis.com/css2?family=Bebas+Neue&family=Poppins:wght@400&display=swap">
<style>
  :root {
    --backdrop: #e6e6e6;
    --cover-edge: #e8ab00;
    --cover-mid: #ecc400;
    --cover-glow: #e8d600;
    --ink: #1d1d1b;
    --art-dark: #151515;
    --art-mid: #5a5a5a;
  }
  * { margin: 0; padding: 0; box-sizing: border-box; }
  html, body {
    width: 1200px;
    height: 800px;
    overflow: hidden;
    background: var(--backdrop);
  }
  .book-cover {
    position: absolute;
    left: 364px;
    top: 40px;
    width: 472px;
    height: 720px;
    background: radial-gradient(ellipse 70% 55% at 50% 52%, var(--cover-glow) 0%, var(--cover-mid) 55%, var(--cover-edge) 100%);
    color: var(--ink);
    font-family: "Bebas Neue", "Oswald", sans-serif;
    font-weight: 400;
    text-align: center;
  }
  .book-title { font-weight: 400; font-size: inherit; }
  .line {
    position: absolute;
    left: 0;
    width: 100%;
    line-height: 1;
    white-space: nowrap;
    font-weight: 400;
  }
  .title-lead   { top: 36px;  font-size: 36px; }
  .title-key    { top: 67px;  font-size: 65px; }
  .title-bridge { top: 122px; font-size: 34px; }
  .title-end    { top: 150px; font-size: 112px; letter-spacing: 1px; }
  .cover-art {
    position: absolute;
    left: 137px;
    top: 273px;
    width: 185px;
    height: 283px;
    border-radius: 92px 92px 40px 40px;
    background: radial-gradient(circle at 45% 35%, var(--art-mid) 0%, var(--art-dark) 75%);
  }
  .series-label {
    top: 586px;
    font-family: "Poppins", sans-serif;
    font-size: 12px;
    letter-spacing: 7px;
    padding-left: 7px;
  }
  .chapter-line { top: 603px; font-size: 46px; }
  .author       { top: 668px; font-size: 36px; }
</style>
</head>
<body>
  <main class="book-cover">
    <h1 class="book-title">
      <span class="line title-lead">WAYS TO</span>
      <span class="line title-key">STAND OUT</span>
      <span class="line title-bridge">AND WHERE YOUR HABITS</span>
      <span class="line title-end">SLIP</span>
    </h1>
    <div class="cover-art" role="img" aria-label="Cover illustration area"></div>
    <p class="line series-label">WAYS TO STAND OUT</p>
    <p class="line chapter-line">TURN THE LAMP INWARD</p>
    <p class="line author">TOBAR KESSLY</p>
  </main>
</body>
</html>
```